Theatre Company needs a Poster design for a world premiere of "Ember Hollow" Play.

We are premiering a play that celebrates community in rural and regional Australia . We need a poster for A3 and A5 size and an image that can be used in our email correspondence/webpage.

Attached is some ideas the producing theatre committee has come up with, a river runs through the town itself.

Town

```html
<!DOCTYPE html>
<html lang="en">
<head>
<meta charset="utf-8">
<title>Ember Hollow — Wattle Bend Theatre Company</title>
<link rel="stylesheet" href="https://fonts.googleapis.com/css2?family=Playfair+Display:wght@700&family=Pinyon+Script&family=Italianno&display=swap">
<style>
  :root {
    --ink: #000000;
    --paper: #ffffff;
    --sky-deep: #0d1a6b;
    --sky-mid: #2b3fb8;
    --sky-violet: #5a4aa8;
    --sunset: #f07a1e;
    --sunset-glow: #ffb347;
    --bank-green: #1f5a2a;
    --water: #1a1a2e;
  }
  html, body {
    margin: 0;
    padding: 0;
    overflow: hidden;
    background: var(--ink);
  }
  .poster {
    position: relative;
    width: 939px;
    height: 1200px;
    background: var(--ink);
    overflow: hidden;
    color: var(--paper);
  }
  .company {
    position: absolute;
    top: 88px;
    left: 0;
    width: 100%;
    margin: 0;
    text-align: center;
    font-family: "Playfair Display", serif;
    font-weight: 700;
    font-size: 36px;
    letter-spacing: 4px;
    transform: scaleX(0.82);
    text-transform: uppercase;
  }
  .presents {
    position: absolute;
    top: 148px;
    left: 0;
    width: 100%;
    margin: 0;
    text-align: center;
    font-family: "Pinyon Script", cursive;
    font-size: 36px;
    letter-spacing: 6px;
  }
  .scene {
    position: absolute;
    left: 106px;
    top: 190px;
    width: 728px;
    height: 912px;
  }
  .title {
    position: absolute;
    top: 900px;
    left: 0;
    width: 100%;
    margin: 0;
    text-align: center;
    font-family: "Pinyon Script", cursive;
    font-weight: 400;
    font-size: 126px;
    line-height: 1;
    text-shadow: 0 0 1px var(--paper), 0 0 1px var(--paper);
  }
  .credit {
    position: absolute;
    top: 1078px;
    left: 0;
    width: 100%;
    margin: 0;
    text-align: center;
    font-family: "Pinyon Script", cursive;
    font-size: 30px;
    letter-spacing: 3px;
  }
</style>
</head>
<body>
  <main class="poster">
    <p class="company">Wattle Bend Theatre Company</p>
    <p class="presents">Presents</p>

    <svg class="scene" viewBox="0 0 728 912" role="img" aria-label="Photograph of a river at sunset winding between tree-lined banks under a deep blue sky, its still water reflecting the orange glow">
      <defs>
        <linearGradient id="scene-tones" x1="0" y1="0" x2="0" y2="1">
          <stop offset="0" stop-color="var(--sky-deep)"/>
          <stop offset="0.22" stop-color="var(--sky-mid)"/>
          <stop offset="0.38" stop-color="var(--sky-violet)"/>
          <stop offset="0.46" stop-color="var(--sunset)"/>
          <stop offset="0.5" stop-color="var(--bank-green)"/>
          <stop offset="0.6" stop-color="var(--sunset)"/>
          <stop offset="0.72" stop-color="var(--water)"/>
          <stop offset="1" stop-color="var(--ink)"/>
        </linearGradient>
        <radialGradient id="scene-vignette" cx="0.5" cy="0.5" r="0.5">
          <stop offset="0.78" stop-color="#000" stop-opacity="0"/>
          <stop offset="1" stop-color="#000" stop-opacity="0.9"/>
        </radialGradient>
      </defs>
      <ellipse cx="364" cy="456" rx="364" ry="456" fill="url(#scene-tones)"/>
      <ellipse cx="364" cy="456" rx="364" ry="456" fill="url(#scene-vignette)"/>
    </svg>

    <h1 class="title">Ember Hollow</h1>
    <p class="credit">Written by DELL MARREN</p>
  </main>
</body>
</html>
```